Hair dresser flyer for Air conditioning heat pumps A5

We require a flyer that is selling the benifits of air conditioning heat pumps which cools in summer and efficently heats in winter. Colour should be white background. Red and blue from logo to represent the Air conditioning Heat pump does heating and cooling and energy effient.

Target Market(s)

Hairdressor, Salons , barbers ,

Colors
0054AA
0677BA
7BADD7
CADEEF
E8F1F8
EB3D1F
EC4F4E
F09395
F8D3D4
FCEDEE

Requirements
Must have
• Cost from

```html
<!DOCTYPE html>
<html lang="en">
<head>
<meta charset="utf-8">
<title>Norland – Air Conditioning Heat Pump Flyer</title>
<link rel="stylesheet" href="https://fonts.googleapis.com/css2?family=Anton&family=Montserrat:wght@400;500;600;700;800&family=Oswald:wght@500;600;700&display=swap">
<style>
  :root {
    --orange: #eb3d1f;
    --blue: #2f9ad8;
    --blue-deep: #0677ba;
    --ink: #0b0b0b;
    --paper: #ffffff;
    --paper-soft: #f4f4f4;
    --stage: #e8f1f8;
    --muted: #555b63;
  }
  * { box-sizing: border-box; margin: 0; padding: 0; }
  html, body { width: 1200px; height: 853px; overflow: hidden; }
  body {
    background: var(--stage);
    font-family: "Montserrat", sans-serif;
    position: relative;
  }
  .flyer {
    position: absolute;
    top: 30px;
    width: 560px;
    height: 792px;
    background: var(--paper);
    overflow: hidden;
    box-shadow: 0 6px 22px rgba(0, 40, 90, .18);
  }
  .flyer--front { left: 30px; }
  .flyer--back { left: 610px; }
  .abs { position: absolute; }

  /* brand name set in the piece's text font */
  .brand { position: absolute; }
  .brand__name { font-weight: 800; font-size: 28px; line-height: 1; color: var(--ink); }
  .brand__tag { font-weight: 600; font-size: 9px; color: var(--ink); margin-top: 5px; }

  .photo { position: absolute; }

  .headline { font-family: "Anton", sans-serif; line-height: 1.15; color: var(--ink); }
  .headline .white { color: var(--paper); }
  .headline .small { font-size: .62em; }

  /* front */
  .front__photo {
    left: 200px; top: 0; width: 360px; height: 215px;
    background: linear-gradient(135deg, #e9c4c0 0%, #d9aaa6 45%, #35432f 70%, #b99a8e 100%);
    clip-path: polygon(20% 0, 100% 0, 100% 100%, 0 100%);
  }
  .front__stripe {
    left: 188px; top: 0; width: 60px; height: 215px; background: var(--ink);
    clip-path: polygon(58% 0, 74% 0, 16% 100%, 0 100%);
  }
  .front__band-top { left: 0; top: 96px; width: 205px; height: 14px; background: var(--blue); clip-path: polygon(0 0, 94% 0, 100% 100%, 0 100%); }
  .front__band-right { left: 360px; top: 198px; width: 200px; height: 30px; background: var(--blue); }
  .front__head {
    left: 0; top: 110px; width: 400px; height: 118px; background: var(--orange);
    clip-path: polygon(0 0, 86% 0, 100% 100%, 0 100%);
    padding: 8px 0 0 24px;
  }
  .front__head .line1 { font-size: 28px; }
  .front__head .line2 { font-size: 23px; }
  .front__head .tag { display: inline-block; background: var(--blue); color: var(--ink); padding: 0 8px; margin-left: 4px; line-height: 1.2; }
  .front__head .line3 { font-size: 26px; color: var(--paper); }
  .front__head .line3 .dark { color: var(--ink); }
  .front__intro {
    left: 24px; top: 238px; width: 390px;
    font-weight: 700; font-size: 21px; line-height: 1.15; color: var(--ink);
  }
  .front__intro .accent { color: var(--blue); }
  .front__body {
    left: 255px; top: 290px; width: 305px; height: 345px; background: var(--blue);
    padding: 16px 16px 0 18px; color: var(--paper); font-size: 10.3px; line-height: 1.45;
  }
  .front__body p + p { margin-top: 12px; }
  .front__offer {
    left: 22px; top: 300px; width: 233px; height: 418px; background: var(--ink);
    padding: 18px 16px 0 18px; color: var(--paper);
  }
  .price { font-weight: 800; color: var(--orange); font-size: 30px; line-height: 1; margin-bottom: 16px; }
  .benefits { list-style: none; }
  .benefits li { display: flex; gap: 8px; align-items: flex-start; font-size: 12.3px; font-weight: 500; margin-bottom: 14px; line-height: 1.2; }
  .benefits svg { flex: none; width: 15px; height: 15px; margin-top: 1px; }

  /* footer */
  .contact { position: absolute; left: 0; right: 0; bottom: 0; height: 74px; border-top: 1px solid #dcdcdc; }
  .contact__title { position: absolute; left: 24px; top: -4px; font-weight: 800; font-size: 29px; color: var(--orange); }
  .contact__rule { position: absolute; left: 24px; top: 33px; width: 68px; height: 4px; background: var(--blue); border-radius: 2px; }
  .contact__item { position: absolute; top: 44px; display: flex; align-items: center; gap: 6px; font-size: 10.5px; color: var(--muted); line-height: 1.2; }
  .contact__item svg { width: 12px; height: 12px; flex: none; }

  /* back */
  .back__photo {
    left: 0; top: 0; width: 560px; height: 240px;
    background: linear-gradient(160deg, #dedad4 0%, #b9aa98 35%, #6e5740 55%, #2a2a2a 80%, #c9c6c0 100%);
  }
  .back__brand-panel { left: 18px; top: 18px; }
  .back__blue {
    left: 0; top: 232px; width: 330px; height: 150px; background: var(--blue);
    clip-path: polygon(0 0, 78% 0, 100% 100%, 0 100%);
    padding: 10px 0 0 18px; font-size: 29px; line-height: 1.12;
  }
  .back__orange {
    left: 252px; top: 222px; width: 308px; height: 160px; background: var(--orange);
    clip-path: polygon(0 0, 100% 0, 100% 100%, 26% 100%);
    padding: 14px 14px 0 60px; color: var(--paper); font-size: 9.2px; line-height: 1.35; text-align: right;
  }
  .back__orange p + p { margin-top: 8px; }
  .back__cool {
    left: 0; top: 382px; width: 560px; height: 40px; background: var(--orange);
    padding: 2px 0 0 18px; font-size: 25px; color: var(--paper);
  }
  .back__cool .dark { color: var(--ink); }
  .back__note {
    left: 0; top: 422px; width: 560px; height: 58px; background: var(--ink); color: var(--paper);
    font-weight: 800; font-size: 12.5px; text-transform: uppercase; text-align: center; line-height: 1.45; padding-top: 9px;
  }
  .compare { font-family: "Oswald", sans-serif; font-weight: 700; text-align: center; line-height: 1.2; }
  .compare .blue { color: var(--blue); }
  .compare .orange { color: var(--orange); }
  .back__heaters { left: 0; top: 480px; width: 560px; height: 96px; background: var(--paper-soft); color: var(--ink); padding-top: 12px; }
  .back__pump { left: 0; top: 576px; width: 560px; height: 130px; background: var(--ink); color: var(--paper); padding-top: 22px; }
  .compare .l1 { font-size: 26px; }
  .compare .l2 { font-size: 28px; }
</style>
</head>
<body>

<!-- Front: offer and benefits -->
<section class="flyer flyer--front">
  <div class="brand" style="left:26px;top:28px">
    <div class="brand__name">Norland</div>
    <div class="brand__tag">Heating and cooling for salons.</div>
  </div>

  <div class="photo front__photo" role="img" aria-label="Photo of a pink salon interior with a lit mirror, green wall and potted palm"></div>
  <div class="abs front__stripe"></div>
  <div class="abs front__band-top"></div>
  <div class="abs front__band-right"></div>

  <h1 class="abs headline front__head">
    <div class="line1">Save £££ <span class="small white">On Your</span></div>
    <div class="line2 white">Shops <span class="tag">Heating Costs</span></div>
    <div class="line3">And Stay <span class="dark">Cool</span> <span class="small">In The Summer</span></div>
  </h1>

  <p class="abs front__intro">Energy- Efficient <span class="accent">Air Conditioning</span><br><span class="accent">Heat Pumps</span> installed from</p>

  <div class="abs front__body">
    <p>Air Conditioning Heat Pumps create the ideal environment all year round for staff to be at their most productive and for customers to spend more time and, accordingly, more money.</p>
    <p>Modern Air Conditioning Heat pumps are one of the most energy efficient forms of heating available and ideal for those looking for a simple cost effective way to heat and cool the space. They are easy to install and operate and can quickly provide the comfort you need.</p>
    <p>Reduce cancelations and absences in the warm summer months with Cooling mode. With warm temperatures inside hairdressers and salons, clients do not want to sit somewhere with extreme heat.</p>
  </div>

  <div class="abs front__offer">
    <div class="price">£1750 + Vat</div>
    <ul class="benefits">
      <li><svg viewBox="0 0 16 16"><rect x="1" y="3" width="12" height="12" fill="none" stroke="#2f9ad8" stroke-width="1.6"/><path d="M3.5 8.5l3 3 8-10" fill="none" stroke="#eb3d1f" stroke-width="2"/></svg>Cools in Summer</li>
      <li><svg viewBox="0 0 16 16"><rect x="1" y="3" width="12" height="12" fill="none" stroke="#2f9ad8" stroke-width="1.6"/><path d="M3.5 8.5l3 3 8-10" fill="none" stroke="#eb3d1f" stroke-width="2"/></svg>Efficient Heats in Winter</li>
      <li><svg viewBox="0 0 16 16"><rect x="1" y="3" width="12" height="12" fill="none" stroke="#2f9ad8" stroke-width="1.6"/><path d="M3.5 8.5l3 3 8-10" fill="none" stroke="#eb3d1f" stroke-width="2"/></svg>More Productive staff</li>
      <li><svg viewBox="0 0 16 16"><rect x="1" y="3" width="12" height="12" fill="none" stroke="#2f9ad8" stroke-width="1.6"/><path d="M3.5 8.5l3 3 8-10" fill="none" stroke="#eb3d1f" stroke-width="2"/></svg>Increased Sales</li>
      <li><svg viewBox="0 0 16 16"><rect x="1" y="3" width="12" height="12" fill="none" stroke="#2f9ad8" stroke-width="1.6"/><path d="M3.5 8.5l3 3 8-10" fill="none" stroke="#eb3d1f" stroke-width="2"/></svg>Reduce cancellation in Summer</li>
      <li><svg viewBox="0 0 16 16"><rect x="1" y="3" width="12" height="12" fill="none" stroke="#2f9ad8" stroke-width="1.6"/><path d="M3.5 8.5l3 3 8-10" fill="none" stroke="#eb3d1f" stroke-width="2"/></svg>Filters and cleans the air</li>
      <li><svg viewBox="0 0 16 16"><rect x="1" y="3" width="12" height="12" fill="none" stroke="#2f9ad8" stroke-width="1.6"/><path d="M3.5 8.5l3 3 8-10" fill="none" stroke="#eb3d1f" stroke-width="2"/></svg>Reduced allergens &amp; Bugs</li>
      <li><svg viewBox="0 0 16 16"><rect x="1" y="3" width="12" height="12" fill="none" stroke="#2f9ad8" stroke-width="1.6"/><path d="M3.5 8.5l3 3 8-10" fill="none" stroke="#eb3d1f" stroke-width="2"/></svg>Reduce Humidity</li>
    </ul>
  </div>

  <footer class="contact">
    <div class="contact__title">Get In Touch</div>
    <div class="contact__rule"></div>
    <div class="contact__item" style="left:26px"><svg viewBox="0 0 12 12"><path d="M2.5 1l2 2.5-1.2 1.3a7 7 0 0 0 3.9 3.9L8.5 7.5 11 9.5 9.6 11C5.5 11 1 6.5 1 2.4z" fill="#2f9ad8"/></svg>01632 960418</div>
    <div class="contact__item" style="left:170px"><svg viewBox="0 0 12 12"><rect x="0.5" y="2" width="11" height="8" fill="#2f9ad8"/><path d="M1 2.5l5 4 5-4" fill="none" stroke="#fff" stroke-width="1"/></svg>www.norlandair.example</div>
    <div class="contact__item" style="left:330px"><svg viewBox="0 0 12 12"><path d="M6 11.5S2 7 2 4.5a4 4 0 0 1 8 0C10 7 6 11.5 6 11.5z" fill="#2f9ad8"/><circle cx="6" cy="4.5" r="1.4" fill="#fff"/></svg><span>Unit 4 Brackenfield Trade Park<br>Brackenfield Road Kelbury KB4 7HT</span></div>
  </footer>
</section>

<!-- Back: running cost comparison -->
<section class="flyer flyer--back">
  <div class="photo back__photo" role="img" aria-label="Photo of a modern hair salon with styling stations, mirrors and a ceiling cassette air conditioning unit"></div>
  <div class="brand back__brand-panel">
    <div class="brand__name">Norland</div>
    <div class="brand__tag">Heating and cooling for salons.</div>
  </div>

  <div class="abs back__orange">
    <p>Reduce heating energy cost by up to 75% vs electric heating. Air conditioning heat pumps is a more efficient heating solution in comparison to a standard electric heaters which are still used in many businesses.</p>
    <p>This is because air conditioning produces more heat for the amount of electricity it takes to power the unit.</p>
  </div>
  <h2 class="abs headline back__blue">
    <div>Save £££</div>
    <div class="white">On Your Shops</div>
    <div>Heating Costs</div>
  </h2>
  <div class="abs headline back__cool">And Stay <span class="dark">Cool</span> <span class="small">In The Summer</span></div>

  <p class="abs back__note">Here's an example to illustrate how an air-to-air<br>heat pump can save you money over an electric heaters</p>

  <div class="abs compare back__heaters">
    <div class="l1 blue">2 x 2kw Electric fan heaters</div>
    <div class="l2"><span class="orange">4kw</span> Electricity input = <span class="orange">4kw</span> heat Output</div>
  </div>
  <div class="abs compare back__pump">
    <div class="l1 blue">4kw Air Conditioning heat pump</div>
    <div class="l2"><span class="orange">1kw</span> Electricity input = <span class="orange">4kw</span> Heat output</div>
  </div>

  <footer class="contact">
    <div class="contact__title">Get In Touch</div>
    <div class="contact__rule"></div>
    <div class="contact__item" style="left:26px"><svg viewBox="0 0 12 12"><path d="M2.5 1l2 2.5-1.2 1.3a7 7 0 0 0 3.9 3.9L8.5 7.5 11 9.5 9.6 11C5.5 11 1 6.5 1 2.4z" fill="#2f9ad8"/></svg>01632 960418</div>
    <div class="contact__item" style="left:170px"><svg viewBox="0 0 12 12"><rect x="0.5" y="2" width="11" height="8" fill="#2f9ad8"/><path d="M1 2.5l5 4 5-4" fill="none" stroke="#fff" stroke-width="1"/></svg>www.norlandair.example</div>
    <div class="contact__item" style="left:330px"><svg viewBox="0 0 12 12"><path d="M6 11.5S2 7 2 4.5a4 4 0 0 1 8 0C10 7 6 11.5 6 11.5z" fill="#2f9ad8"/><circle cx="6" cy="4.5" r="1.4" fill="#fff"/></svg><span>Unit 4 Brackenfield Trade Park<br>Brackenfield Road Kelbury KB4 7HT</span></div>
  </footer>
</section>

</body>
</html>
```